High End Notary Service Business Card Design

Want a professional and elegant/luxurious business card that is clean and simple in the design. A notary is a trusted professional that helps people sign very important documents. The card should be in alignment with this service provided.

Most of the time, service will be for the purchase of a home or refinance of a mortgage

There is NO LOGO. This is aesthetic. A look and feel. Conveying professionalism and concierge level of service.

Target Market(s)

Other business professionals, Lawyers, Escrow Officers, Loan Officers

Industry/Entity Type

Legal

Contact Information for Business Card

This will be a one-sided business card

Colors
35a7d7
3176b5
85cae6
d3a5cc
b868aa
ffffff
0356a4

Requirements
Must have
• Lorena T. Mirabel-Hodgkins
Notary Public

642-871-3094
MirabelSigningDesk@Wexmail.com
Nice to have
• Headshot photo below. Convey the aspect of signing documents. No black cards. Preference is shades of blue: light blue, navy, aqua, gold, white, or lavendar, etc.
Should not have
• No scales or legal scales.

```html
<!DOCTYPE html>
<html lang="en">
<head>
<meta charset="utf-8">
<title>Lorena T. Mirabel-Hodgkins — Notary Public</title>
<link rel="stylesheet" href="https://fonts.googleapis.com/css2?family=Jost:wght@400;500&display=swap">
<style>
  :root {
    --backdrop: #cfcfcf;
    --card-white: #ffffff;
    --notary-blue: #0356a4;
    --ring-blue: #85cae6;
    --portrait-light: #b4b4b4;
    --portrait-dark: #6e6e6e;
    --text-light: #ffffff;
  }
  * { margin: 0; padding: 0; box-sizing: border-box; }
  html, body {
    width: 1200px;
    height: 900px;
    overflow: hidden;
    background: var(--backdrop);
  }
  .business-card {
    position: absolute;
    left: 427px;
    top: 147px;
    width: 346px;
    height: 606px;
    border-radius: 18px;
    overflow: hidden;
    background: linear-gradient(to bottom, var(--card-white) 0, var(--card-white) 178px, var(--notary-blue) 178px);
    font-family: "Jost", "Futura", sans-serif;
    color: var(--text-light);
    text-align: center;
  }
  .portrait {
    position: absolute;
    left: 1px;
    top: 6px;
    width: 344px;
    height: 344px;
    border-radius: 50%;
    border: 2px solid var(--ring-blue);
    background: radial-gradient(circle at 50% 45%, var(--portrait-light) 0%, #9a9a9a 55%, var(--portrait-dark) 100%);
  }
  .holder-name {
    position: absolute;
    top: 420px;
    left: 0;
    width: 100%;
    font-size: 17.5px;
    font-weight: 400;
    letter-spacing: 0.2px;
    text-transform: uppercase;
  }
  .holder-title {
    position: absolute;
    top: 442px;
    left: 0;
    width: 100%;
    font-size: 14.5px;
    letter-spacing: 0.4px;
  }
  .contact-icons {
    position: absolute;
    top: 475px;
    left: 0;
    width: 100%;
    display: flex;
    justify-content: center;
    gap: 8px;
  }
  .contact-icons svg { width: 18px; height: 18px; }
  .contact-lines {
    position: absolute;
    top: 505px;
    left: 0;
    width: 100%;
    font-size: 14px;
    line-height: 21px;
    letter-spacing: 0.4px;
  }
</style>
</head>
<body>
  <div class="business-card">
    <div class="portrait" role="img" aria-label="Black and white headshot of the notary"></div>
    <p class="holder-name">Lorena T. Mirabel-Hodgkins</p>
    <p class="holder-title">Notary Public</p>
    <div class="contact-icons">
      <svg viewBox="0 0 18 18" aria-label="Phone" role="img">
        <circle cx="9" cy="9" r="8.2" fill="none" stroke="#fff" stroke-width="1.1"/>
        <path d="M6.3 4.6l1.4-.3.9 2.2-.9.8c.4 1.4 1.3 2.6 2.5 3.4l.9-.7 2 1.1-.4 1.4c-3.5.2-6.9-3.9-6.4-7.9z" fill="none" stroke="#fff" stroke-width="1" stroke-linejoin="round"/>
      </svg>
      <svg viewBox="0 0 18 18" aria-label="Email" role="img">
        <circle cx="9" cy="9" r="8.2" fill="none" stroke="#fff" stroke-width="1.1"/>
        <rect x="4.8" y="6" width="8.4" height="6" rx="0.8" fill="none" stroke="#fff" stroke-width="1"/>
        <path d="M5 6.4l4 3 4-3" fill="none" stroke="#fff" stroke-width="1"/>
      </svg>
    </div>
    <div class="contact-lines">
      <p class="contact-phone">642-871-3094</p>
      <p class="contact-email">MirabelSigningDesk@Wexmail.com</p>
    </div>
  </div>
</body>
</html>
```